Breezeway Climate Business Card Design

Design new, 2 sides, business cards for a residential and light commercial heating, air conditioning contractor.

Target Market(s)

Homeowners, small businesses

Industry/Entity Type

Business

Contact Information for Business Card

Dominic Vasquerelli
Phone - 555-214-6837
Email
Address - PO box 618
Millbrook NJ 07999
Website - www.BreezewayClimateLLC.example

Requirements
Must have
• logo, company colors, standard size with no die cut, so I can use printhaven

```html
<!DOCTYPE html>
<html lang="en">
<head>
<meta charset="utf-8">
<title>Breezeway Climate Business Card</title>
<link rel="stylesheet" href="https://fonts.googleapis.com/css2?family=Source+Sans+3:wght@400;600;700&display=swap">
<style>
  :root {
    --crimson: #a02032;
    --amber: #f0922a;
    --ink: #3f3f3f;
    --paper: #ffffff;
    --backdrop: #e9e6e2;
  }
  * { margin: 0; padding: 0; box-sizing: border-box; }
  html, body {
    width: 1200px; height: 987px; overflow: hidden;
    background: var(--backdrop);
    font-family: "Source Sans 3", sans-serif;
  }
  .card {
    position: absolute; left: 293px; width: 615px; height: 352px;
    box-shadow: 0 2px 6px rgba(0,0,0,.18);
  }
  .card-front { top: 130px; background: var(--paper); }
  .card-back { top: 506px; background: var(--crimson); }

  .brand {
    position: absolute; display: flex; align-items: center; gap: 10px;
    font-weight: 700; font-size: 27px; line-height: 1; white-space: nowrap;
  }
  .card-front .brand { right: 32px; top: 100px; color: var(--crimson); }
  .card-back .brand { right: 36px; top: 245px; color: var(--paper); }
  .brand-dot { width: 16px; height: 16px; border-radius: 50%; background: var(--amber); }

  .name-bar { position: absolute; left: 0; top: 173px; width: 12px; height: 47px; background: var(--crimson); }
  .name {
    position: absolute; left: 34px; top: 170px;
    font-size: 22px; font-weight: 600; color: var(--crimson); letter-spacing: .2px;
  }
  .title { position: absolute; left: 34px; top: 197px; font-size: 17px; color: var(--amber); }
  .rule { position: absolute; left: 34px; right: 32px; top: 223px; height: 2px; background: var(--amber); }

  .contacts { position: absolute; left: 34px; top: 240px; list-style: none; }
  .contacts li {
    display: flex; align-items: center; gap: 9px;
    font-size: 16px; color: var(--ink); height: 22px; white-space: nowrap;
  }
  .contacts svg { width: 15px; height: 15px; fill: var(--crimson); flex: none; }

  .address {
    position: absolute; right: 32px; top: 252px; text-align: right;
    font-size: 16px; font-style: normal; color: var(--ink); line-height: 22.5px;
    white-space: nowrap;
  }
  .address .web { letter-spacing: .4px; }
</style>
</head>
<body>
  <section class="card card-front">
    <div class="brand">Breezeway Climate<span class="brand-dot"></span></div>
    <div class="name-bar"></div>
    <h1 class="name">DOMINIC VASQUERELLI</h1>
    <p class="title">CEO/Founder</p>
    <div class="rule"></div>
    <ul class="contacts">
      <li><svg viewBox="0 0 16 16"><path d="M3.5 1l2.6 3-1.4 2a9 9 0 0 0 5 5l2-1.4 3 2.6-1.6 2.6C7 15 1 9 .9 2.6z"/></svg>555 214 6837</li>
      <li><svg viewBox="0 0 16 16"><path d="M4 0h8a1 1 0 0 1 1 1v14a1 1 0 0 1-1 1H4a1 1 0 0 1-1-1V1a1 1 0 0 1 1-1zm1 2v10h6V2zm3 11a1 1 0 1 0 0 2 1 1 0 0 0 0-2z"/></svg>555 382 1094</li>
      <li><svg viewBox="0 0 16 16"><path d="M4 1h8v4H4zM1 6h14v7h-2v-2H3v2H1zm3 6h8v3H4z"/></svg>555 760 2251</li>
      <li><svg viewBox="0 0 16 16"><path d="M1 4h14v9H1zm1 1.2v.4l6 4 6-4v-.4z"/></svg>name@breezeway.example</li>
    </ul>
    <address class="address">
      PO box 618<br>
      Millbrook NJ 07999<br>
      <span class="web">www.BreezewayClimateLLC.example</span>
    </address>
  </section>

  <section class="card card-back">
    <div class="brand">Breezeway Climate<span class="brand-dot"></span></div>
  </section>
</body>
</html>
```